Website design and coding for new consultancy company

I need to have a full website designed for a new consultancy business I'm trying to establish. It's called Brightpath consult. I need an English version to begin with, and then there should be a Danish version as well, but I'll translate that myself. Just be aware that I need two language versions. The consultancy field that I'm targeting is Leadership - and specialist development. I offer to facilitate corporate academies for global companies as well as specific workshops within leadership- or team development, strategy sessions, personal coaching and facilitation of D&I (Diversity and inclusion) workshops. BTW my logo is not in high resolution - I need that as well.

Target Market(s)

Larger companies that has a need for developing their inhouse leadership capabilities or that wants to develop their specialists to take on more responsibility.

Industry/Entity Type

Consultancy business

Coding

Number of Pages Required

5+ page

Requirements
Must have
• Introduction site with a catch phrase. Book a meeting. Services that's beeing offered. Blog site with white papers etc. Language toggle (Danish/English). Cases/testimonials. About site. Contact site.

```html
<!DOCTYPE html>
<html lang="en">
<head>
<meta charset="utf-8">
<title>Brightpath Consult – Management that works in practice</title>
<link href="https://fonts.googleapis.com/css2?family=Bebas+Neue&family=Oswald:wght@500;600;700&family=Montserrat:wght@400;500;600&display=swap" rel="stylesheet">
<style>
  :root{
    --navy:#0c1a29;
    --navy-deep:#09141f;
    --blue:#1f86d6;
    --white:#ffffff;
    --ink:#0c1a29;
    --muted:#5d6670;
    --card:#f0f2f4;
    --rule:#3c4a59;
  }
  *{margin:0;padding:0;box-sizing:border-box}
  html,body{width:1200px;height:2981px;overflow:hidden;background:var(--white)}
  body{position:relative;font-family:"Montserrat",sans-serif;color:var(--ink)}
  .abs{position:absolute}
  .display{font-family:"Bebas Neue",sans-serif;font-weight:400;letter-spacing:0.2px}
  .cond{font-family:"Oswald",sans-serif;font-weight:600;letter-spacing:-0.8px;text-transform:uppercase}

  /* Hero */
  .hero{left:0;top:0;width:1200px;height:719px;background:linear-gradient(120deg,var(--navy) 0%,var(--navy-deep) 100%)}
  .brand{display:flex;align-items:center;gap:12px;color:var(--white);font-family:"Bebas Neue",sans-serif;font-size:54px;line-height:1;white-space:nowrap}
  .brand-mark{width:16px;height:16px;background:var(--blue)}
  .site-header .brand{left:90px;top:24px}
  .nav{top:42px;left:0;width:1200px;height:30px}
  .nav a{position:absolute;color:var(--white);font-size:14px;text-decoration:none;transform:translateX(-50%);white-space:nowrap}
  .nav a.active{border-bottom:2px solid var(--blue);padding-bottom:4px}
  .lang{left:958px;top:30px;width:152px;height:42px;background:var(--blue);color:var(--white);display:flex;align-items:center;justify-content:center;gap:8px;font-size:14px;font-weight:500}
  .flag{width:30px;height:18px;background:#2c4f9e;border:2px solid #fff}
  .header-rule{left:90px;top:103px;width:1020px;height:2px;background:var(--rule)}
  .hero-title{left:90px;top:258px;z-index:2;color:var(--white);font-size:68px;line-height:64px;letter-spacing:-1.5px;white-space:nowrap}
  .hero-text{left:90px;top:402px;width:410px;z-index:2;color:var(--white);font-size:14.5px;line-height:22px}
  .btn{display:flex;align-items:center;justify-content:center;font-size:14.5px;font-weight:600;text-decoration:none;white-space:nowrap}
  .btn-blue{background:var(--blue);color:var(--white)}
  .btn-white{background:var(--white);color:var(--ink);font-weight:500}
  .hero-btn{left:90px;top:488px;width:165px;height:42px;z-index:2}
  .portrait{left:548px;top:127px;width:563px;height:592px;z-index:1;background:linear-gradient(180deg,#b99478 0%,#8d7364 40%,#2f4260 75%,#23324a 100%)}

  /* Services */
  .section-title{width:1200px;left:0;text-align:center;color:var(--ink)}
  .services-title{top:806px;font-size:56px;line-height:60px}
  .card{width:288px;height:288px;top:891px;background:var(--card);text-align:center}
  .card-icon{position:absolute;left:106px;top:39px;width:77px;height:67px;background:var(--blue);display:flex;align-items:center;justify-content:center}
  .card h3{position:absolute;top:122px;width:100%;font-size:20px;line-height:26px}
  .card p{position:absolute;top:154px;left:26px;width:236px;font-size:13.5px;line-height:22px;color:var(--muted)}
  .card-arrow{position:absolute;left:126px;top:272px;width:37px;height:32px;background:var(--navy);display:flex;align-items:center;justify-content:center}
  .more-btn{left:507px;top:1231px;width:187px;height:42px}

  /* Leadership */
  .lead-title{top:1356px;font-size:58px;line-height:60px}
  .lead-sub{top:1420px;font-size:19px;line-height:26px}
  .team-photo{left:149px;top:1495px;width:435px;height:344px;background:linear-gradient(135deg,#c7ccd2 0%,#8e959e 45%,#2e3440 100%)}
  .purpose{left:633px;width:420px}
  .purpose h4{font-size:18px;line-height:24px;color:var(--ink)}
  .purpose p{font-size:13.5px;line-height:22px;color:var(--muted);margin-top:2px}
  .cta-band{left:274px;top:1901px;width:652px;height:58px;background:var(--blue);color:var(--white);font-size:20px}

  /* Empowering */
  .emp-title{left:90px;top:2096px;font-size:58px;line-height:56px;color:var(--ink)}
  .emp-text{left:92px;top:2277px;width:510px;font-size:13.5px;line-height:22px;color:var(--muted)}
  .meeting-photo{left:675px;top:2066px;width:435px;height:344px;background:linear-gradient(140deg,#e6ddd3 0%,#bfa894 45%,#3a3f4c 100%)}

  /* Footer */
  .footer{left:0;top:2526px;width:1200px;height:455px;background:linear-gradient(120deg,var(--navy) 0%,var(--navy-deep) 100%)}
  .footer .brand{left:90px;top:160px;font-size:72px;gap:16px}
  .footer .brand-mark{width:20px;height:20px}
  .footer-title{left:523px;top:64px;color:var(--white);font-size:58px;line-height:60px;white-space:nowrap}
  .footer-text{left:524px;top:254px;color:var(--white);font-size:14.5px;line-height:20px}
  .footer-btn{left:524px;top:284px;width:188px;height:42px}
  .footer-rule{left:90px;top:395px;width:1020px;height:1px;background:var(--rule)}
  .copyright{left:0;top:418px;width:1200px;text-align:center;color:var(--white);font-size:14.5px}
</style>
</head>
<body>

<section class="hero abs">
  <header class="site-header">
    <div class="brand abs"><span class="brand-mark"></span>Brightpath</div>
    <nav class="nav abs">
      <a href="#" class="active" style="left:567px">Home</a>
      <a href="#" style="left:668px">About Us</a>
      <a href="#" style="left:771px">Service</a>
      <a href="#" style="left:881px">Contact Us</a>
    </nav>
    <div class="lang abs"><span class="flag"></span>English
      <svg width="10" height="7" viewBox="0 0 10 7"><path d="M1 1l4 4 4-4" fill="none" stroke="#fff" stroke-width="1.6"/></svg>
    </div>
    <div class="header-rule abs"></div>
  </header>
  <div class="portrait abs" role="img" aria-label="Portrait photo of the consultant in a navy blazer"></div>
  <h1 class="hero-title display abs">Management that<br>works in practice</h1>
  <p class="hero-text abs">I help specialists and managers take even more responsibility, set clear direction and create effective collaborations.</p>
  <a href="#" class="btn btn-blue hero-btn abs">Book A Meeting</a>
</section>

<h2 class="section-title services-title display abs">Our Services</h2>

<article class="card abs" style="left:148px">
  <div class="card-icon"><svg width="40" height="34" viewBox="0 0 40 34" fill="none" stroke="#fff" stroke-width="1.8"><path d="M4 12l16-7 16 7-16 7z"/><path d="M10 15v7c4 3 16 3 20 0v-7"/><path d="M2 26h36v4H2z"/></svg></div>
  <h3 class="cond">Corporate Academies</h3>
  <p>Tailored learning programs to build long-term leadership and specialist capabilities across your organization.</p>
  <div class="card-arrow"><svg width="8" height="12" viewBox="0 0 8 12"><path d="M2 1l5 5-5 5" fill="none" stroke="#fff" stroke-width="1.8"/></svg></div>
</article>

<article class="card abs" style="left:456px">
  <div class="card-icon"><svg width="40" height="36" viewBox="0 0 40 36" fill="none" stroke="#fff" stroke-width="1.8"><rect x="4" y="3" width="32" height="20" rx="2"/><path d="M12 10h16M12 15h10"/><circle cx="11" cy="29" r="3"/><circle cx="20" cy="29" r="3"/><circle cx="29" cy="29" r="3"/></svg></div>
  <h3 class="cond">Strategy Sessions</h3>
  <p>Facilitation of executive and team strategy workshops, enabling clarity and alignment on key goals.</p>
  <div class="card-arrow"><svg width="8" height="12" viewBox="0 0 8 12"><path d="M2 1l5 5-5 5" fill="none" stroke="#fff" stroke-width="1.8"/></svg></div>
</article>

<article class="card abs" style="left:764px">
  <div class="card-icon"><svg width="36" height="38" viewBox="0 0 36 38" fill="none" stroke="#fff" stroke-width="1.8"><circle cx="18" cy="12" r="7"/><path d="M4 36c0-9 6-14 14-14s14 5 14 14z"/></svg></div>
  <h3 class="cond">Personal Coaching</h3>
  <p>One-on-one coaching to support leaders in building resilience, confidence, and effective decision-making.</p>
  <div class="card-arrow"><svg width="8" height="12" viewBox="0 0 8 12"><path d="M2 1l5 5-5 5" fill="none" stroke="#fff" stroke-width="1.8"/></svg></div>
</article>

<a href="#" class="btn btn-blue more-btn abs">View More Service</a>

<h2 class="section-title lead-title display abs">Leadership is not about titles</h2>
<p class="section-title lead-sub cond abs">It’s about taking responsibility for the business, collaboration and development</p>

<div class="team-photo abs" role="img" aria-label="Photo of three smiling businesswomen with arms crossed in an office"></div>

<div class="purpose abs" style="top:1526px">
  <h4 class="cond">The purpose of Brightpath</h4>
  <p>I help organizations get the full potential out of their organization whether it's about leaders, specialists or teams. I work with practical measures that create impact development not just inspiration.</p>
</div>
<div class="purpose abs" style="top:1666px">
  <h4 class="cond">Specialists with increased responsibility</h4>
  <p>We see companies that continue to place greater responsibility on their specialists, why I see it as a necessity that companies not only invest in management development, but also gives their specialists a necessary competence boost they can take on greater responsibilities.</p>
</div>

<a href="#" class="btn cta-band cond abs">Curious about how we work with managers &amp; specialists in practice?</a>

<h2 class="emp-title display abs">Empowering<br>specialists with greater<br>responsibility</h2>
<p class="emp-text abs">We see companies placing more responsibility on specialists. Brightpath helps organisations invest in both leadership development and specialist competency so teams can perform stronger and deliver impact.</p>
<div class="meeting-photo abs" role="img" aria-label="Photo of a team of colleagues gathered around a desk reviewing documents"></div>

<footer class="footer abs">
  <div class="brand abs"><span class="brand-mark"></span>Brightpath</div>
  <h2 class="footer-title display abs">Curious about how we work<br>with leaders and specialists<br>in practice?</h2>
  <p class="footer-text abs">Book a meeting to discuss a tailored programe for your organisation.</p>
  <a href="#" class="btn btn-white footer-btn abs">Book A Meeting</a>
  <div class="footer-rule abs"></div>
  <p class="copyright abs">© "Brightpath Consult" 2025</p>
</footer>

</body>
</html>
```